Marlows Pet Care

Hi. I need a business card /logo for my pet care business. Im thinking about a dogs paw print. Although i do look after other pets so don't want to restrict my self. Open to suggestions on colour etc but like greens and purples.The name of my business is marlow's pet care. The logo could be just an image or have marlows power care on it. An option to do either would be great. For the winner i also would like a Web page (word press template if possible) designed if you can, of course I'll pay additional for this. Look forward to your ideas!

```html
<!DOCTYPE html>
<html lang="en">
<head>
<meta charset="utf-8">
<title>Marlow's Pet Care – Business Card</title>
<link rel="stylesheet" href="https://fonts.googleapis.com/css2?family=Open+Sans:wght@400;600&display=swap">
<style>
  :root {
    --backdrop: #2b2b2e;
    --card: #1b1b1f;
    --purple: #6a2d9c;
    --purple-deep: #55207f;
    --green: #7cc242;
    --silver: #a9a9b1;
    --white: #f2f2f2;
  }
  * { margin: 0; padding: 0; box-sizing: border-box; }
  html, body {
    width: 1200px; height: 800px; overflow: hidden;
    background: var(--backdrop);
    font-family: "Open Sans", sans-serif;
  }
  .stage {
    width: 1200px; height: 800px;
    display: flex; align-items: center; justify-content: center;
  }
  .business-card {
    position: relative;
    width: 840px; height: 480px;
    background: var(--card);
    border-radius: 20px;
    overflow: hidden;
    box-shadow: 0 18px 40px rgba(0,0,0,.45);
  }
  .emblem-area {
    position: absolute; inset: 0;
    width: 840px; height: 480px;
  }
  .brand {
    position: absolute; left: 52px; top: 44px;
    display: flex; align-items: flex-start; gap: 14px;
  }
  .brand-dot {
    width: 22px; height: 22px; border-radius: 50%;
    background: var(--green); margin-top: 20px;
  }
  .brand-name {
    color: var(--purple);
    font-weight: 600;
    font-size: 58px; line-height: 1.02;
    letter-spacing: -0.5px;
  }
  .holder {
    position: absolute; left: 52px; top: 218px;
  }
  .holder-name {
    color: var(--purple);
    font-size: 34px; font-weight: 400; letter-spacing: 1px;
    line-height: 1;
  }
  .holder-role {
    color: var(--white); font-size: 17px; margin-top: 4px;
  }
  .contact-list {
    position: absolute; left: 52px; top: 300px;
    list-style: none;
  }
  .contact-item {
    display: flex; align-items: center; gap: 12px;
    color: var(--white); font-size: 19px; height: 34px;
  }
  .contact-icon {
    width: 20px; height: 20px; flex: none;
  }
</style>
</head>
<body>
<main class="stage">
  <section class="business-card">
    <svg class="emblem-area" viewBox="0 0 840 480" aria-hidden="false">
      <defs>
        <radialGradient id="emblem-fill" cx="50%" cy="50%" r="50%">
          <stop offset="0%" stop-color="#b3b3bb"/>
          <stop offset="60%" stop-color="#9d9aa8"/>
          <stop offset="100%" stop-color="#6a2d9c"/>
        </radialGradient>
      </defs>
      <circle cx="640" cy="320" r="300" fill="url(#emblem-fill)" role="img" aria-label="Decorative pet emblem illustration"/>
    </svg>

    <div class="brand">
      <span class="brand-dot"></span>
      <h1 class="brand-name">Marlow's<br>Pet Care</h1>
    </div>

    <div class="holder">
      <p class="holder-name">MARLOW</p>
      <p class="holder-role">Director</p>
    </div>

    <ul class="contact-list">
      <li class="contact-item">
        <svg class="contact-icon" viewBox="0 0 20 20"><rect width="20" height="20" rx="3" fill="var(--purple)"/><path d="M6 4h3l1 3-2 1.5a8 8 0 0 0 3.5 3.5L13 10l3 1v3a2 2 0 0 1-2 2A11 11 0 0 1 4 6a2 2 0 0 1 2-2z" fill="var(--card)"/></svg>
        (304) 555-0182
      </li>
      <li class="contact-item">
        <svg class="contact-icon" viewBox="0 0 20 20"><rect width="20" height="20" rx="3" fill="var(--purple)"/><rect x="4" y="6" width="12" height="8" fill="var(--card)"/><path d="M4 6l6 5 6-5" fill="none" stroke="var(--purple)" stroke-width="1.4"/></svg>
        Marlow@marlowspetcare.co.uk
      </li>
      <li class="contact-item">
        <svg class="contact-icon" viewBox="0 0 20 20"><rect width="20" height="20" rx="3" fill="var(--purple)"/></svg>
        /marlowspetcare
      </li>
      <li class="contact-item">
        <svg class="contact-icon" viewBox="0 0 20 20"><rect width="20" height="20" rx="3" fill="var(--purple)"/><circle cx="10" cy="10" r="6" fill="none" stroke="var(--card)" stroke-width="1.4"/><path d="M4 10h12M10 4c-3 3-3 9 0 12M10 4c3 3 3 9 0 12" fill="none" stroke="var(--card)" stroke-width="1.2"/></svg>
        www.marlowspetcare.co.uk
      </li>
    </ul>
  </section>
</main>
</body>
</html>
```